Real Estate Agent Service Brochure

I need a trifold brochure to showcase my real estate services. I am a veteran Real Estate Broker specializing in marketing properties for sale and for top dollar. I would like to see designs that use colors from my logo (attached) and I would like to showcase some before and after photos of staging jobs I have done to homes to get them ready for the market. This brochure is specific to home sellers. You are happy to go check out my website for inspiration www.lumbrava-homes.example but keep the copy as I have written it. The the final design should communicate experienced professional who uses current technologies and strategies to market properties for the highest value.

Target Market(s)

Homeowners wanting to sell their homes

Industry/Entity Type

Real Estate Agent

Font styles to use
Serif

Requirements
Must have
• My, logo, personal photo, title and contact information as listed:
• Marta Valenko
• Owner Broker
• Stager Re-Designer
• 555-218-9064
• BRAVO Realty LLC
• LUMBRAVA-HOMES.example
• Marta@LUMBRAVA-HOMES.example
• The colors used should be those in my logo.
• Brochure should be able to fit in standard envelope for mailing.
Nice to have
• I think I would like my personal photo and contact information on the front panel.
Should not have
• Bright colors.

```html
<!DOCTYPE html>
<html lang="en">
<head>
<meta charset="utf-8">
<title>BRAVO Realty LLC – Seller Brochure</title>
<link href="https://fonts.googleapis.com/css2?family=Open+Sans:ital,wght@0,400;0,600;0,700;1,400&display=swap" rel="stylesheet">
<style>
  :root{
    --stage:#dedede;
    --charcoal:#58595b;
    --charcoal-dark:#4a4b4d;
    --navy:#1f3366;
    --paper:#ffffff;
    --paper-shade:#ececec;
    --ink:#3b3b3d;
    --ink-soft:#5d5e60;
  }
  *{box-sizing:border-box;margin:0;padding:0}
  html,body{width:1200px;height:2397px;overflow:hidden}
  body{background:var(--stage);font-family:"Open Sans",Arial,sans-serif;color:var(--ink);position:relative}

  .spread{position:absolute;left:50px;width:1100px;height:850px;display:grid;grid-template-columns:repeat(3,1fr);
    background:var(--paper);box-shadow:0 14px 30px rgba(0,0,0,.18)}
  .spread--outside{top:230px}
  .spread--inside{top:1320px}
  .panel{position:relative;overflow:hidden;background:linear-gradient(180deg,var(--paper) 60%,var(--paper-shade))}
  .panel + .panel{border-left:1px solid #d4d4d4}

  .band{position:absolute;left:0;right:0;background:var(--charcoal)}
  .band--foot{bottom:0;height:34px}
  .photo{position:absolute;left:0;right:0}

  .brand{font-weight:700;letter-spacing:1px;text-transform:uppercase;display:flex;align-items:center;gap:10px}
  .brand__mark{width:14px;height:14px;border-radius:50%;background:currentColor}
  .brand--light{color:#fff}
  .brand--navy{color:var(--navy)}

  .copy p{font-size:12.5px;line-height:1.55;color:var(--ink-soft);margin-bottom:12px}

  .contact{list-style:none}
  .contact li{display:flex;align-items:center;gap:8px;font-size:13px;color:var(--ink);line-height:1.9}
  .contact svg{width:16px;height:16px;flex:none}
  .contact--right li{justify-content:flex-end}

  /* outside: testimonials */
  .testimonials__head{position:absolute;top:0;left:0;right:0;height:96px;background:var(--charcoal);padding:26px 26px 0;
    color:#fff;font-style:italic;font-size:17px;line-height:1.35}
  .testimonials .copy{position:absolute;top:118px;left:26px;right:26px}
  .testimonials .copy p{font-size:11.5px;margin-bottom:14px}

  /* outside: back panel */
  .back__top{top:0;height:58px;display:flex;align-items:center;justify-content:center;color:#fff;font-size:12px;letter-spacing:.5px}
  .back__info{position:absolute;top:600px;left:40px;right:30px}
  .back__info .brand{font-size:30px;margin-bottom:14px}

  /* outside: front panel */
  .front__top{top:0;height:150px;display:flex;align-items:center;justify-content:center}
  .front__top .brand{font-size:32px}
  .front__title{position:absolute;top:525px;left:26px;right:0;height:96px;background:var(--navy);color:#fff;
    display:flex;align-items:center;justify-content:center;text-align:center;font-size:24px;line-height:1.2;letter-spacing:1px}
  .front__who{position:absolute;top:640px;right:26px;text-align:right}
  .front__name{font-size:21px;color:var(--ink)}
  .front__role{font-size:13px;font-weight:600;color:var(--ink);margin:2px 0 8px}
  .front__who .contact li{font-size:12px;line-height:1.75}

  /* inside */
  .intro__brand{position:absolute;top:34px;left:0;right:0;display:flex;justify-content:center}
  .intro__brand .brand{font-size:30px}
  .intro .copy{position:absolute;top:100px;left:28px;right:28px}
  .mid .copy{position:absolute;top:440px;left:28px;right:28px}
  .close .copy{position:absolute;top:440px;left:28px;right:28px}
  .close__web{position:absolute;left:40px;right:0;bottom:80px;height:40px;background:var(--navy);color:#fff;
    font-size:12px;display:flex;align-items:center;justify-content:flex-end;padding-right:26px;letter-spacing:.4px}
</style>
</head>
<body>

<!-- Outside of the trifold -->
<section class="spread spread--outside">
  <article class="panel testimonials">
    <h2 class="testimonials__head">This is what Marta's clients say about their experiences:</h2>
    <div class="copy">
      <p>"Marta and her team made the sale of our family home feel simple. She staged every room with care and we had several offers within the first week on the market."</p>
      <p>"We were nervous about selling after so many years. Marta explained each step, priced the house with confidence and found buyers who truly loved it."</p>
      <p>"Her staging advice changed how our home looked online. The photos were beautiful, showings were busy and we closed above our asking price."</p>
      <p>"Professional, patient and always reachable. Marta knows the local market and uses every modern tool to get a home in front of the right buyers."</p>
    </div>
    <div class="photo" style="top:640px;height:176px;background:linear-gradient(160deg,#3a3f36,#7a4a33 55%,#c48a5a)" role="img" aria-label="Photo of a lit brick and timber house at dusk surrounded by autumn trees"></div>
    <div class="band band--foot"></div>
  </article>

  <article class="panel back">
    <div class="band back__top">www.lumbrava-homes.example</div>
    <div class="photo" style="top:58px;height:500px;background:linear-gradient(135deg,#eae6df,#cfc6b8 45%,#8f7a66 80%,#5e4a3d)" role="img" aria-label="Staged living room with white built-in shelving, a corner fireplace and a cream sofa"></div>
    <div class="back__info">
      <div class="brand brand--navy"><span class="brand__mark"></span>BRAVO Realty LLC</div>
      <ul class="contact">
        <li><svg viewBox="0 0 16 16"><circle cx="8" cy="8" r="8" fill="#1f3366"/><path d="M5.2 4.2l1.5 0 .6 2-1 .8a5 5 0 0 0 2.7 2.7l.8-1 2 .6v1.5c0 .4-.4.8-.8.8A7.5 7.5 0 0 1 4.4 5c0-.4.4-.8.8-.8z" fill="#fff"/></svg>555-218-9064</li>
        <li><svg viewBox="0 0 16 16"><circle cx="8" cy="8" r="8" fill="#1f3366"/><rect x="4" y="5" width="8" height="6" fill="none" stroke="#fff" stroke-width="1"/><path d="M4 5l4 3.2L12 5" fill="none" stroke="#fff" stroke-width="1"/></svg>Marta@LUMBRAVA-HOMES.example</li>
        <li><svg viewBox="0 0 16 16"><circle cx="8" cy="8" r="8" fill="#1f3366"/><circle cx="8" cy="8" r="4" fill="none" stroke="#fff" stroke-width="1"/><path d="M4 8h8M8 4c-2 2.4-2 5.6 0 8M8 4c2 2.4 2 5.6 0 8" fill="none" stroke="#fff" stroke-width=".8"/></svg>www.LUMBRAVA-HOMES.example</li>
      </ul>
    </div>
    <div class="band band--foot"></div>
  </article>

  <article class="panel front">
    <div class="band front__top"><div class="brand brand--light"><span class="brand__mark"></span>BRAVO Realty LLC</div></div>
    <div class="photo" style="top:150px;height:420px;background:linear-gradient(160deg,#e9e4dc,#c9bba8 45%,#2a2a2e 75%,#3a3a40)" role="img" aria-label="Portrait of the broker in a dark blazer standing in a staged living room"></div>
    <h1 class="front__title">PROVEN MARKET<br>KNOWLEDGE</h1>
    <div class="front__who">
      <div class="front__name">Marta Valenko</div>
      <div class="front__role">Owner Broker - Stage Re-Designer</div>
      <ul class="contact contact--right">
        <li>555-218-9064<svg viewBox="0 0 16 16"><circle cx="8" cy="8" r="8" fill="#1f3366"/><path d="M5.2 4.2l1.5 0 .6 2-1 .8a5 5 0 0 0 2.7 2.7l.8-1 2 .6v1.5c0 .4-.4.8-.8.8A7.5 7.5 0 0 1 4.4 5c0-.4.4-.8.8-.8z" fill="#fff"/></svg></li>
        <li>Marta@LUMBRAVA-HOMES.example<svg viewBox="0 0 16 16"><circle cx="8" cy="8" r="8" fill="#1f3366"/><rect x="4" y="5" width="8" height="6" fill="none" stroke="#fff" stroke-width="1"/><path d="M4 5l4 3.2L12 5" fill="none" stroke="#fff" stroke-width="1"/></svg></li>
        <li>www.LUMBRAVA-HOMES.example<svg viewBox="0 0 16 16"><circle cx="8" cy="8" r="8" fill="#1f3366"/><circle cx="8" cy="8" r="4" fill="none" stroke="#fff" stroke-width="1"/><path d="M4 8h8M8 4c-2 2.4-2 5.6 0 8M8 4c2 2.4 2 5.6 0 8" fill="none" stroke="#fff" stroke-width=".8"/></svg></li>
      </ul>
    </div>
    <div class="band band--foot"></div>
  </article>
</section>

<!-- Inside of the trifold -->
<section class="spread spread--inside">
  <article class="panel intro">
    <div class="intro__brand"><div class="brand brand--navy"><span class="brand__mark"></span>BRAVO Realty LLC</div></div>
    <div class="copy">
      <p>Selling Real Estate has changed dramatically in the last few years. Today's real estate processes are multi-faceted, requiring understanding that encompasses significant emotional and financial commitments. Having the right marketing partner is so important, one who works to protect your best interests while guiding you through the many complexities of the real estate transaction.</p>
      <p>Marta Valenko, Real Estate Marketing Specialist, truly understands not only the legal process needed but also recognizes buyer trends and knows how to "showcase" a property to set it apart. A home is one of your most valuable assets. If you are thinking about selling a property, it is crucial that you hire someone with an extraordinary history of happy sellers.</p>
    </div>
    <div class="photo" style="top:560px;height:256px;background:linear-gradient(135deg,#f1efea,#c9c3b8 50%,#a06a3c)" role="img" aria-label="Kitchen shown half as a design sketch and half as the finished staged room"></div>
    <div class="band band--foot"></div>
  </article>

  <article class="panel mid">
    <div class="photo" style="top:30px;left:26px;right:0;height:250px;background:linear-gradient(135deg,#d8d2c8,#8d7a68 55%,#5a4a3e)" role="img" aria-label="Staged dining and living area before listing"></div>
    <div class="photo" style="top:290px;left:26px;width:160px;height:120px;background:linear-gradient(135deg,#cfc8bc,#7a6858)" role="img" aria-label="Small staging photo of a bedroom"></div>
    <div class="photo" style="top:290px;left:196px;right:0;height:120px;background:linear-gradient(135deg,#e4ded4,#9a8a78)" role="img" aria-label="Small staging photo of a sitting room"></div>
    <div class="copy">
      <p>Marta devotes her efforts to selling real estate by keeping up with the evolving market, researching buyer trends and preparing homes before they enter the market by staging them to connect with the target buyer.</p>
      <p>Marta knows all sales are not alike. Therefore, taking a cookie cutter approach is not acceptable. She recognizes that each property is unique and requires a personalized marketing plan and strategy.</p>
      <p>A veteran in the real estate industry with nearly 30 years of expertise and a consistent top producer record, combined with her certified Home Stager and Re-Designer credentials, assures her clients get the advantage of value.</p>
    </div>
    <div class="band band--foot"></div>
  </article>

  <article class="panel close">
    <div class="photo" style="top:30px;left:0;right:26px;height:250px;background:linear-gradient(135deg,#ece7df,#b9a890 50%,#6d5a48)" role="img" aria-label="Staged living room with a wooden coffee table and framed artwork"></div>
    <div class="photo" style="top:290px;left:0;width:160px;height:120px;background:linear-gradient(135deg,#d6cfc4,#857260)" role="img" aria-label="Small staging photo of an entry hall"></div>
    <div class="photo" style="top:290px;left:170px;right:26px;height:120px;background:linear-gradient(135deg,#e0d9cd,#8f7c68)" role="img" aria-label="Small staging photo of a family room"></div>
    <div class="copy">
      <p>Knowledge, seasoned experience and proven results are all geared to creating beautiful spaces which form an emotional connection with the right buyer, producing the highest and best offer.</p>
      <p>This is what you can expect when you work with Proven Market Knowledge.</p>
      <p>The sale of a home is too important an undertaking to entrust to just anyone. Select a dedicated, results-driven broker who understands the intricacies of the Real Estate process.</p>
    </div>
    <div class="close__web">www.LUMBRAVA-HOMES.example</div>
    <div class="band band--foot"></div>
  </article>
</section>

</body>
</html>
```